Eye Catching Email Marketing design

Our health care consulting firm is based in New York City. We sell health care consulting Services to medical practices (doctors). We need a powerful email marketing design to use as one of our primary selling tools to attract new clients. The Design should convey health care knowledge, expertise professionalism, cutting edge technology and the services we offer. <br/>The design should incorporate our logo and its colors (blue and white) but we want it to be eye catching and vibrant, so other colors be included. We are open to the designer's creativity. Any pictures used should show diversity (races)and should include women. Designers can find our logo and other graphics on our website at www larkfield advisory group.com. Please feel free to ask questions.<br/><br/>

Target Market(s)

Health care professionals, executives and Doctors.

Colors

Designer to choose colors to be used in the design.

Requirements
Nice to have
• What ever the design feels will help make this design vibrant

```html
<!DOCTYPE html>
<html lang="en">
<head>
<meta charset="utf-8">
<title>Larkfield Advisory Group – Email</title>
<link href="https://fonts.googleapis.com/css2?family=Merriweather:wght@300;400&family=Open+Sans:wght@400;600;700&display=swap" rel="stylesheet">
<style>
  :root{
    --page:#dcdcdc;
    --paper:#ffffff;
    --brand:#2f62ad;
    --band:#2a5db0;
    --accent:#2b8fd0;
    --tile:#efefef;
    --soft:#f3f3f3;
    --ink:#3a3a3a;
    --muted:#555555;
  }
  *{box-sizing:border-box;margin:0;padding:0}
  html,body{width:1200px;height:5080px;overflow:hidden;background:var(--page)}
  body{position:relative;font-family:"Open Sans",Arial,sans-serif;color:var(--ink)}
  .email{position:absolute;left:144px;top:56px;width:912px;height:4756px;background:var(--paper)}
  .masthead{height:256px;display:flex;align-items:center;justify-content:center;gap:22px}
  .masthead-mark{width:34px;height:34px;background:var(--brand)}
  .masthead-name{font-family:"Merriweather",Georgia,serif;font-weight:400;font-size:34px;color:var(--brand);letter-spacing:1px}
  .hero-photo{margin:0 16px;height:576px;background:linear-gradient(160deg,#d9c7a8 0%,#b58a62 40%,#5b3a2a 70%,#e8e1d8 100%)}
  .hero-band{margin:0 16px;height:192px;background:var(--band);color:#fff;display:flex;align-items:center;justify-content:center;text-align:center;padding:0 48px;font-weight:700;font-size:25px;line-height:1.55}
  .about{padding-top:66px;text-align:center;height:428px}
  .section-title{font-family:"Merriweather",Georgia,serif;font-weight:300;color:var(--brand);font-size:62px;line-height:1.2}
  .lede{font-size:21px;line-height:1.6;color:var(--muted);padding:14px 26px 0;text-align:center}
  .services{margin:0 16px;display:grid;grid-template-columns:432px 432px;grid-auto-rows:352px;column-gap:16px;row-gap:24px}
  .service{background:var(--tile);display:flex;flex-direction:column;align-items:center;padding-top:50px}
  .service svg{width:120px;height:120px}
  .service-name{margin-top:40px;font-family:"Merriweather",Georgia,serif;font-weight:300;font-size:42px;line-height:1.3;text-align:center;color:var(--ink)}
  .expertise{margin-top:116px;height:960px;background:var(--soft);padding-top:92px;text-align:center}
  .expertise .section-title{font-size:60px;line-height:1.15}
  .expertise .lede{padding:24px 40px 0}
  .expertise-photo{position:absolute;left:0;right:0;top:2684px;height:572px;background:linear-gradient(90deg,#f3f3f3 0%,#e7e4e1 35%,#cdb8aa 55%,#eae6e3 80%,#f3f3f3 100%)}
  .news{padding-top:100px}
  .news .section-title{text-align:center;font-size:62px;margin-bottom:46px}
  .news-item{margin:0 16px 28px;height:228px;display:flex;background:var(--tile)}
  .news-date{flex:0 0 168px;width:168px;background:var(--accent);color:#fff;display:flex;flex-direction:column;align-items:center;justify-content:center}
  .news-day{font-family:"Merriweather",Georgia,serif;font-weight:400;font-size:80px;line-height:1}
  .news-month{font-size:24px;margin-top:18px;letter-spacing:1px}
  .news-body{flex:1 1 auto;min-width:0;padding:40px 90px 0 48px}
  .news-title{font-family:"Merriweather",Georgia,serif;font-weight:400;font-size:27px;line-height:1.45;color:#222;text-transform:uppercase}
  .news-title.plain{text-transform:none;font-size:30px}
  .news-text{margin-top:14px;font-size:19px;line-height:1.55;color:var(--muted)}
  .closing{text-align:center;padding-top:110px}
  .closing-title{font-family:"Merriweather",Georgia,serif;font-weight:300;font-size:46px;line-height:1.4;color:#222}
  .cta{display:inline-block;margin-top:40px;width:352px;height:112px;line-height:112px;background:var(--accent);color:#fff;font-family:"Merriweather",Georgia,serif;font-weight:300;font-size:36px;letter-spacing:1px}
  .footer{position:absolute;left:0;top:4850px;width:1200px;text-align:center;font-size:20px;line-height:2.1;color:#333}
  .social{display:flex;justify-content:center;gap:36px;margin-top:32px}
  .social span{width:80px;height:80px;border:3px solid #999;border-radius:50%}
</style>
</head>
<body>
<div class="email">
  <header class="masthead">
    <span class="masthead-mark"></span>
    <span class="masthead-name">LARKFIELD ADVISORY GROUP LLC</span>
  </header>

  <div class="hero-photo" role="img" aria-label="Photo of a smiling female doctor in a white coat with a stethoscope, city office behind her"></div>
  <div class="hero-band">Larkfield Advisory Group specializes in Revenue Cycle Management, Practice Management, Compliance Management &amp; Healthcare Innovation.</div>

  <section class="about">
    <h2 class="section-title">About LAG</h2>
    <p class="lede">Larkfield Advisory Group (LAG), founded in 2015, is a Management Services Organization &amp; Healthcare Consulting Firm skilled at helping medical practices advance their strategic vision in an ever-evolving healthcare system. Larkfield Advisory Group specializes in Revenue Cycle Management, Practice Management, Compliance Management &amp; Healthcare Innovation.</p>
  </section>

  <section class="services">
    <div class="service">
      <svg viewBox="0 0 60 60" fill="none" stroke="#2b8fd0" stroke-width="6">
        <path d="M48 22a20 20 0 0 0-34-6"/><path d="M12 38a20 20 0 0 0 34 6"/>
        <path d="M10 8v10h10" stroke-linejoin="round"/><path d="M50 52V42H40" stroke-linejoin="round"/>
      </svg>
      <div class="service-name">Revenue Cycle<br>Management</div>
    </div>
    <div class="service">
      <svg viewBox="0 0 60 60" fill="#2b8fd0">
        <path d="M14 6h32v48H14z" opacity=".9"/>
        <path d="M30 18l10 4v8c0 7-5 11-10 13-5-2-10-6-10-13v-8z" fill="#fff"/>
        <path d="M25 30l4 4 7-7" stroke="#2b8fd0" stroke-width="3" fill="none"/>
      </svg>
      <div class="service-name">Compliance<br>Management</div>
    </div>
    <div class="service">
      <svg viewBox="0 0 60 60" fill="#2b8fd0">
        <circle cx="30" cy="22" r="14"/><circle cx="30" cy="22" r="6" fill="#fff"/>
        <path d="M8 56c0-12 9-18 22-18s22 6 22 18z"/>
      </svg>
      <div class="service-name">Healthcare<br>Innovation</div>
    </div>
    <div class="service">
      <svg viewBox="0 0 60 60" fill="none" stroke="#2b8fd0" stroke-width="5" stroke-linecap="round">
        <path d="M6 30l8 16h12"/><path d="M54 30l-8 16H34"/>
        <circle cx="30" cy="20" r="8"/><path d="M30 4v4M30 32v4M14 20h4M42 20h4"/>
      </svg>
      <div class="service-name">Practice<br>Management</div>
    </div>
  </section>

  <section class="expertise">
    <h2 class="section-title">Expertise Your<br>Medical Practice Deserves</h2>
    <p class="lede">Ms. Dorsey founded Larkfield Advisory Group in 2015 to help medical practices develop and advance their strategic vision in an ever evolving and increasingly complex health care environment.</p>
  </section>
  <div class="expertise-photo" role="img" aria-label="Photo of a female doctor in a white coat reading a tablet"></div>

  <section class="news">
    <h2 class="section-title">News</h2>
    <article class="news-item">
      <div class="news-date"><span class="news-day">18</span><span class="news-month">FEB</span></div>
      <div class="news-body">
        <h3 class="news-title">Common Problems in Medical Coding</h3>
        <p class="news-text">The coder's job is to code to the highest level of specificity.</p>
      </div>
    </article>
    <article class="news-item">
      <div class="news-date"><span class="news-day">22</span><span class="news-month">FEB</span></div>
      <div class="news-body">
        <h3 class="news-title">Revenue Cycle Challenges</h3>
        <p class="news-text">Here are the most common pain points for the Medical Practices revenue cycle and tips for providers about how to avoid financial trouble.</p>
      </div>
    </article>
    <article class="news-item">
      <div class="news-date"><span class="news-day">26</span><span class="news-month">FEB</span></div>
      <div class="news-body">
        <h3 class="news-title plain">$999,000 HIPAA Settlement</h3>
        <p class="news-text">Unauthorized Disclosure of Patients' Protected Health Information During "Harbor Clinic" Filming Results in Multiple HIPAA Settlements Totaling $999,000</p>
      </div>
    </article>
  </section>

  <section class="closing">
    <h2 class="closing-title">Advancing Healthcare<br>Operations</h2>
    <span class="cta">CONTACT US</span>
  </section>
</div>

<footer class="footer">
  <p>Copyright © 2020 Larkfield Advisory Group LLC.<br>All rights reserved.</p>
  <div class="social"><span></span><span></span><span></span></div>
</footer>
</body>
</html>
```